Lumo Quest - Main Menu - Re-Design

I want to have a refresh for this app's main menu. There are some different items on the menu depending on the language (English vs. Non-English) and version (Pro vs. Free). I have attached screenshots of the different conditions. This app is a collection of brain training games.

Need designs for light and dark mode. Need designs for both portrait and landscape mode.

Here is a link to the app in Vexo Shelf.
https://shelf.vexomarket.test/store/apps/details?id=tarnwick.lumoquest

Here is a link to the app in the Quorra App Depot.
https://apps.quorradepot.test/us/app/lumo-quest-brain-training/id573918204?ls=1&mt=8

```html
<!DOCTYPE html>
<html lang="en">
<head>
<meta charset="utf-8">
<title>Lumo Quest Pro – Main Menu</title>
<link rel="stylesheet" href="https://fonts.googleapis.com/css2?family=Merriweather:wght@700&family=Poppins:ital,wght@0,400;0,500;1,300&display=swap">
<style>
  :root {
    --backdrop: #cdd3d7;
    --screen: #0e1030;
    --tile: #ffffff;
    --tile-text: #1b1c2e;
    --light-text: #ffffff;
    --home-bar: #5a5d78;
    --logo-a: #2a7fe0;
    --logo-b: #0d3f9a;
    --brain-a: #f06b9a;
    --brain-b: #f5c64a;
    --brain-c: #6fcf97;
    --brain-d: #4fb6e8;
    --ink: #23253a;
    --coral: #f07b6b;
    --peach: #f6b48a;
    --sun: #f7c64a;
    --orange: #f19a4a;
    --leaf: #6cb96f;
    --teal: #4fb0ad;
    --sky: #4fb6e8;
    --steel: #c9ced8;
  }
  * { box-sizing: border-box; margin: 0; padding: 0; }
  html, body { width: 1200px; height: 552px; overflow: hidden; }
  body { background: var(--backdrop); position: relative; font-family: "Poppins", sans-serif; }

  .sprite { position: absolute; width: 0; height: 0; overflow: hidden; }

  .screen { position: absolute; background: var(--screen); border-radius: 20px; color: var(--light-text); overflow: hidden; }
  .screen--portrait { width: 188px; height: 413px; top: 69px; }
  .screen--landscape { width: 413px; height: 189px; left: 717px; }
  .screen--splash-p { left: 108px; }
  .screen--menu-p { left: 357px; }
  .screen--splash-l { top: 61px; }
  .screen--menu-l { top: 308px; }

  .status { position: absolute; left: 0; right: 0; height: 12px; display: flex; align-items: center; justify-content: space-between; padding: 0 12px 0 14px; font-size: 9px; }
  .screen--portrait .status { top: 13px; }
  .screen--landscape .status { top: 4px; padding: 0 20px 0 24px; }
  .status__time { position: absolute; left: 50%; transform: translateX(-50%); letter-spacing: .3px; }
  .status__icons { display: flex; gap: 3px; align-items: flex-end; }

  .home-bar { position: absolute; left: 50%; transform: translateX(-50%); width: 59px; height: 2px; border-radius: 2px; background: var(--home-bar); }

  .app-mark { position: absolute; border-radius: 50%; background: radial-gradient(circle at 35% 35%, var(--logo-a), var(--logo-b)); box-shadow: 0 0 0 2px rgba(42,127,224,.35); }

  .title { position: absolute; font-family: "Merriweather", serif; font-weight: 700; font-size: 22px; line-height: 24px; text-align: center; }
  .tagline { position: absolute; font-style: italic; font-weight: 300; font-size: 11.5px; text-align: center; }
  .signup { position: absolute; font-size: 6px; text-align: center; }

  .brain-art { position: absolute; border-radius: 48% 52% 46% 54% / 55% 50% 50% 45%;
    background: linear-gradient(120deg, var(--brain-a) 0%, var(--brain-b) 35%, var(--brain-c) 60%, var(--brain-d) 100%); opacity: .9; }

  .tile { position: absolute; width: 71px; height: 58px; background: var(--tile); border-radius: 4px; color: var(--tile-text); display: flex; flex-direction: column; align-items: center; justify-content: flex-end; padding-bottom: 8px; font-size: 7.5px; font-weight: 500; white-space: nowrap; }
  .tile__icon { width: 28px; height: 26px; margin-bottom: 5px; }
</style>
</head>
<body>

<svg class="sprite" aria-hidden="true">
  <defs>
    <symbol id="i-training" viewBox="0 0 28 26">
      <rect x="3" y="8" width="4" height="10" rx="1" fill="var(--coral)" stroke="var(--ink)" stroke-width="1"/>
      <rect x="21" y="8" width="4" height="10" rx="1" fill="var(--coral)" stroke="var(--ink)" stroke-width="1"/>
      <rect x="7" y="10" width="3" height="6" rx=".8" fill="var(--peach)" stroke="var(--ink)" stroke-width="1"/>
      <rect x="18" y="10" width="3" height="6" rx=".8" fill="var(--peach)" stroke="var(--ink)" stroke-width="1"/>
      <rect x="10" y="12" width="8" height="2" fill="var(--steel)" stroke="var(--ink)" stroke-width="1"/>
    </symbol>
    <symbol id="i-games" viewBox="0 0 28 26">
      <path d="M7 7h14c3 0 5 3 5.5 8s-2 7-4 5l-3-3H8.5l-3 3c-2 2-4.5 0-4-5S4 7 7 7z" fill="var(--steel)" stroke="var(--ink)" stroke-width="1.2"/>
      <path d="M8 10v5M5.5 12.5h5" stroke="var(--ink)" stroke-width="1.4"/>
      <circle cx="19" cy="11" r="1.2" fill="var(--coral)"/><circle cx="21.5" cy="13.5" r="1.2" fill="var(--sky)"/>
    </symbol>
    <symbol id="i-schedule" viewBox="0 0 28 26">
      <rect x="3" y="4" width="18" height="17" rx="1.5" fill="#fff" stroke="var(--ink)" stroke-width="1.2"/>
      <rect x="3" y="4" width="18" height="4" fill="var(--coral)" stroke="var(--ink)" stroke-width="1.2"/>
      <g fill="var(--ink)"><circle cx="7" cy="11" r=".9"/><circle cx="10" cy="11" r=".9"/><circle cx="13" cy="11" r=".9"/><circle cx="7" cy="14" r=".9"/><circle cx="10" cy="14" r=".9"/><circle cx="7" cy="17" r=".9"/></g>
      <circle cx="19.5" cy="17.5" r="5.5" fill="var(--sky)" stroke="var(--ink)" stroke-width="1.2"/>
      <path d="M17 17.5l2 2 3-3.5" fill="none" stroke="#fff" stroke-width="1.4"/>
    </symbol>
    <symbol id="i-learning" viewBox="0 0 28 26">
      <path d="M14 5a6.5 6.5 0 0 0-4 11.6V19h8v-2.4A6.5 6.5 0 0 0 14 5z" fill="var(--sun)" stroke="var(--ink)" stroke-width="1.2"/>
      <rect x="10.5" y="19" width="7" height="3" rx=".8" fill="var(--steel)" stroke="var(--ink)" stroke-width="1"/>
      <g stroke="var(--ink)" stroke-width="1" stroke-linecap="round"><path d="M14 1v2M5 4l1.5 1.5M23 4l-1.5 1.5M2 11h2M24 11h2"/></g>
    </symbol>
    <symbol id="i-settings" viewBox="0 0 28 26">
      <path d="M14 2l2 3 3.5-.8.6 3.5 3.3 1.5-1.5 3.3 1.5 3.3-3.3 1.5-.6 3.5-3.5-.8-2 3-2-3-3.5.8-.6-3.5-3.3-1.5 1.5-3.3-1.5-3.3 3.3-1.5.6-3.5 3.5.8z" fill="var(--steel)" stroke="var(--ink)" stroke-width="1.1"/>
      <circle cx="14" cy="13" r="4.5" fill="var(--leaf)" stroke="var(--ink)" stroke-width="1.1"/>
    </symbol>
    <symbol id="i-more" viewBox="0 0 28 26">
      <rect x="4" y="3" width="9" height="9" rx="2" fill="var(--sun)" stroke="var(--ink)" stroke-width="1.1"/>
      <rect x="15" y="3" width="9" height="9" rx="2" fill="var(--orange)" stroke="var(--ink)" stroke-width="1.1"/>
      <rect x="4" y="14" width="9" height="9" rx="2" fill="var(--orange)" stroke="var(--ink)" stroke-width="1.1"/>
      <path d="M19.5 15v7M16 18.5h7" stroke="var(--ink)" stroke-width="1.5" stroke-linecap="round"/>
    </symbol>
    <symbol id="i-upgrade" viewBox="0 0 28 26">
      <path d="M8 19a5 5 0 0 1-.5-10A7 7 0 0 1 21 9a5 5 0 0 1 0 10z" fill="#bfe8e6" stroke="var(--ink)" stroke-width="1.2"/>
      <path d="M14 23v-10M10.5 16l3.5-3.5 3.5 3.5" fill="none" stroke="var(--teal)" stroke-width="2" stroke-linecap="round" stroke-linejoin="round"/>
    </symbol>
    <symbol id="i-scores" viewBox="0 0 28 26">
      <rect x="4" y="14" width="4.5" height="8" fill="var(--coral)" stroke="var(--ink)" stroke-width="1"/>
      <rect x="11.5" y="9" width="4.5" height="13" fill="var(--sun)" stroke="var(--ink)" stroke-width="1"/>
      <rect x="19" y="5" width="4.5" height="17" fill="var(--sky)" stroke="var(--ink)" stroke-width="1"/>
      <path d="M2 22.5h24" stroke="var(--ink)" stroke-width="1.2"/>
      <path d="M4 10l7-5 5 3 7-6" fill="none" stroke="var(--leaf)" stroke-width="1.3"/>
    </symbol>
    <symbol id="s-wifi" viewBox="0 0 8 8"><path d="M1 3a4.3 4.3 0 0 1 6 0M2.2 4.4a2.5 2.5 0 0 1 3.6 0" fill="none" stroke="#fff" stroke-width=".9"/><circle cx="4" cy="6.3" r=".7" fill="#fff"/></symbol>
    <symbol id="s-signal" viewBox="0 0 8 7"><g fill="#fff"><rect x="0" y="5" width="1.5" height="2"/><rect x="2.2" y="3.5" width="1.5" height="3.5"/><rect x="4.4" y="2" width="1.5" height="5"/><rect x="6.6" y="0" width="1.4" height="7"/></g></symbol>
    <symbol id="s-battery" viewBox="0 0 5 8"><g fill="#fff"><rect x="1.3" y="0" width="2.4" height="1"/><rect x="0" y="1" width="5" height="7" rx=".6"/></g></symbol>
  </defs>
</svg>

<!-- Portrait splash -->
<section class="screen screen--portrait screen--splash-p">
  <div class="status">
    <svg width="8" height="8"><use href="#s-wifi"/></svg>
    <span class="status__time">22:14</span>
    <span class="status__icons"><svg width="8" height="7"><use href="#s-signal"/></svg><svg width="5" height="8"><use href="#s-battery"/></svg></span>
  </div>
  <div class="app-mark" style="left:73px;top:61px;width:42px;height:42px"></div>
  <h1 class="title" style="left:0;right:0;top:131px">Lumo<br>Quest Pro</h1>
  <p class="tagline" style="left:0;right:0;top:178px">exercise your brain</p>
  <div class="brain-art" role="img" aria-label="Colourful brain illustration" style="left:12px;top:218px;width:163px;height:137px"></div>
  <p class="signup" style="left:0;right:0;top:370px">Sign up an account</p>
  <div class="home-bar" style="top:400px"></div>
</section>

<!-- Portrait menu -->
<section class="screen screen--portrait screen--menu-p">
  <div class="status">
    <svg width="8" height="8"><use href="#s-wifi"/></svg>
    <span class="status__time">22:14</span>
    <span class="status__icons"><svg width="8" height="7"><use href="#s-signal"/></svg><svg width="5" height="8"><use href="#s-battery"/></svg></span>
  </div>
  <div class="app-mark" style="left:74px;top:40px;width:42px;height:42px"></div>
  <div class="tile" style="left:17px;top:93px"><svg class="tile__icon"><use href="#i-training"/></svg>Training Center</div>
  <div class="tile" style="left:101px;top:93px"><svg class="tile__icon"><use href="#i-games"/></svg>Games List</div>
  <div class="tile" style="left:17px;top:164px"><svg class="tile__icon"><use href="#i-schedule"/></svg>Schedule</div>
  <div class="tile" style="left:101px;top:164px"><svg class="tile__icon"><use href="#i-learning"/></svg>Learning</div>
  <div class="tile" style="left:17px;top:237px"><svg class="tile__icon"><use href="#i-settings"/></svg>Settings</div>
  <div class="tile" style="left:101px;top:237px"><svg class="tile__icon"><use href="#i-more"/></svg>More Apps</div>
  <div class="tile" style="left:17px;top:308px"><svg class="tile__icon"><use href="#i-upgrade"/></svg>Upgrade</div>
  <div class="tile" style="left:101px;top:308px"><svg class="tile__icon"><use href="#i-scores"/></svg>Scores</div>
  <div class="home-bar" style="top:400px"></div>
</section>

<!-- Landscape splash -->
<section class="screen screen--landscape screen--splash-l">
  <div class="status">
    <svg width="8" height="8"><use href="#s-wifi"/></svg>
    <span class="status__time">22:14</span>
    <span class="status__icons"><svg width="8" height="7"><use href="#s-signal"/></svg><svg width="5" height="8"><use href="#s-battery"/></svg></span>
  </div>
  <div class="app-mark" style="left:39px;top:74px;width:42px;height:42px"></div>
  <h1 class="title" style="left:91px;width:140px;top:59px">Lumo<br>Quest Pro</h1>
  <p class="tagline" style="left:91px;width:140px;top:111px">exercise your brain</p>
  <div class="brain-art" role="img" aria-label="Colourful brain illustration" style="left:242px;top:37px;width:152px;height:128px"></div>
  <p class="signup" style="left:156px;width:100px;top:155px">Sign up an account</p>
  <div class="home-bar" style="top:171px"></div>
</section>

<!-- Landscape menu -->
<section class="screen screen--landscape screen--menu-l">
  <div class="status">
    <svg width="8" height="8"><use href="#s-wifi"/></svg>
    <span class="status__time">22:14</span>
    <span class="status__icons"><svg width="8" height="7"><use href="#s-signal"/></svg><svg width="5" height="8"><use href="#s-battery"/></svg></span>
  </div>
  <div class="app-mark" style="left:10px;top:84px;width:22px;height:22px"></div>
  <div class="tile" style="left:47px;top:28px"><svg class="tile__icon"><use href="#i-training"/></svg>Training Center</div>
  <div class="tile" style="left:133px;top:28px"><svg class="tile__icon"><use href="#i-games"/></svg>Games List</div>
  <div class="tile" style="left:218px;top:28px"><svg class="tile__icon"><use href="#i-schedule"/></svg>Schedule</div>
  <div class="tile" style="left:304px;top:28px"><svg class="tile__icon"><use href="#i-learning"/></svg>Learning</div>
  <div class="tile" style="left:47px;top:102px"><svg class="tile__icon"><use href="#i-settings"/></svg>Settings</div>
  <div class="tile" style="left:133px;top:102px"><svg class="tile__icon"><use href="#i-more"/></svg>More Apps</div>
  <div class="tile" style="left:218px;top:102px"><svg class="tile__icon"><use href="#i-upgrade"/></svg>Upgrade</div>
  <div class="tile" style="left:304px;top:102px"><svg class="tile__icon"><use href="#i-scores"/></svg>Scores</div>
  <div class="home-bar" style="top:177px"></div>
</section>

</body>
</html>
```